Corporate Power Point Template

Tarnel Holdings, Inc. produces and sells ready-mixed concrete, aggregates, and concrete-related products and services for the construction industry in the United States.

We are looking for a simple and sleek design that will look great on a projector, as well as when printed on paper. We prefer a lighter background color that will not waste ink when printed. We would also like to stay away from wavy banners, or over-the-top graphics that take away from usable space in the deck. Please use a variation of the color scheme in the "Brand Standards" file attached.

Construction

```html
<!DOCTYPE html>
<html lang="en">
<head>
<meta charset="utf-8">
<title>Tarnel Holdings — Presentation Template</title>
<link href="https://fonts.googleapis.com/css2?family=Roboto:ital,wght@0,300;0,400;0,500;0,700;1,300;1,400&display=swap" rel="stylesheet">
<style>
:root{
  --red:#c8102e;
  --dark-red:#8e0f1a;
  --black:#141414;
  --ink:#3c3c3c;
  --grey:#8a8a8a;
  --light:#bdbdbd;
  --pale:#ececec;
  --gap:#d6d6d6;
}
*{box-sizing:border-box;margin:0;padding:0}
html,body{width:1058px;height:1200px;overflow:hidden;background:var(--gap)}
body{font-family:"Roboto",Arial,sans-serif;color:var(--ink)}
.deck{width:1058px;height:1200px;display:grid;grid-template-columns:repeat(3,1fr);grid-template-rows:repeat(6,1fr);gap:3px 4px}
.slide{position:relative;background:#fff;overflow:hidden}
.slide::before{content:"";position:absolute;left:0;top:0;bottom:0;width:8px;background:var(--red);box-shadow:inset -2px 0 0 var(--dark-red)}
.a{position:absolute}
.title{left:24px;top:13px;font-size:8.5px;font-weight:500;letter-spacing:.5px;color:#555;text-transform:uppercase}
.num{right:9px;top:3px;width:14px;height:19px;background:var(--red);color:#fff;font-size:4px;display:flex;align-items:center;justify-content:center}
.p{font-size:3.6px;line-height:1.45;color:var(--grey);text-align:justify}
.p.dk{color:#555}
.b{font-weight:700}
.red{color:var(--red)}
.bar-red{background:var(--red);color:#fff}
.center{text-align:center}

/* cover */
.brand-name{left:44px;top:62px;font-size:24px;font-weight:700;color:#777;letter-spacing:-.5px;line-height:1}
.brand-sub{left:45px;top:87px;font-size:10px;color:#777;letter-spacing:1.6px;font-weight:400}
.cover-title{left:45px;top:108px;font-size:10.5px;font-weight:700;color:#8a8a8a}
.cover-sub{left:45px;top:121px;font-size:6.5px;color:#9a9a9a}
.cover-url{left:45px;top:141px;width:132px;height:9px;font-size:5px;font-weight:700;display:flex;align-items:center;justify-content:center}

/* agenda */
.agenda-item{width:98px}
.agenda-no{width:14px;height:14px;color:#fff;font-size:5px;font-weight:700;display:flex;align-items:center;justify-content:center;float:left;margin:4px 4px 0 0}
.agenda-item small{display:block;font-size:2.8px;color:var(--grey)}
.agenda-item strong{display:block;font-size:5.6px;font-weight:700;color:var(--black);border-bottom:.5px solid #555;padding-bottom:1px}
.agenda-item span{display:block;font-size:2.8px;color:var(--grey);line-height:1.4;margin-top:1px}
.bg-black{background:var(--black)}.bg-red{background:var(--red)}.bg-dred{background:var(--dark-red)}

.photo{background:linear-gradient(160deg,#8c8c8c,#4a4a4a)}

/* team */
.team-strip{left:8px;right:0;top:100px;bottom:0;background:var(--red);display:flex;flex-direction:column;gap:1px}
.team-row{display:flex;gap:1px;height:48px}
.team-row.top{background:#2a2a2a}
.team-photo{position:relative;width:calc((100% - 5px)/6);height:48px;background:linear-gradient(160deg,#9a9a9a,#3e3e3e)}
.team-photo b{position:absolute;left:2px;top:2px;width:7px;height:5px;background:var(--red);color:#fff;font-size:2.6px;display:flex;align-items:center;justify-content:center}

/* table */
.report td,.report th{font-size:3.4px;color:var(--grey);padding:1.8px 0;border-bottom:.4px solid #ddd;text-align:left;font-weight:400}
.report th{color:var(--red);font-size:4.4px;border-bottom:.6px solid var(--red)}
.stats{right:0;top:56px;width:76px;bottom:0;background:var(--black)}
.stats h4{font-size:4.6px;color:#fff;font-weight:700;padding:5px 8px}
.stat{background:var(--red);color:#fff;margin:0 0 3px 0;padding:3px 8px;font-size:3.6px;height:21px}
.stat b{display:block;font-size:4.6px}
</style>
</head>
<body>
<main class="deck">

<!-- 1 Cover -->
<section class="slide">
  <div class="a brand-name">TARNEL</div>
  <div class="a brand-sub">HOLDINGS</div>
  <div class="a cover-title">Presentation Template</div>
  <div class="a cover-sub">Some description of subtitle here</div>
  <div class="a cover-url bar-red">www.tarnel-holdings.com</div>
</section>

<!-- 2 Agenda -->
<section class="slide">
  <div class="a title">Presentation Agenda</div><div class="a num">2</div>
  <div class="a agenda-item" style="left:24px;top:48px"><div class="agenda-no bg-black">01</div><small>Subtitle of agenda</small><strong>Presentation Topic</strong><span>Maecenas venenatis faucibus lectus, quis iaculis orci tincidunt auctor.</span></div>
  <div class="a agenda-item" style="left:24px;top:86px"><div class="agenda-no bg-red">02</div><small>Subtitle of agenda</small><strong>Presentation Topic</strong><span>Maecenas venenatis faucibus lectus, quis iaculis orci tincidunt auctor.</span></div>
  <div class="a agenda-item" style="left:24px;top:123px"><div class="agenda-no bg-red">03</div><small>Subtitle of agenda</small><strong>Presentation Topic</strong><span>Maecenas venenatis faucibus lectus, quis iaculis orci tincidunt auctor.</span></div>
  <div class="a agenda-item" style="left:130px;top:48px"><div class="agenda-no bg-red">04</div><small>Subtitle of agenda</small><strong>Presentation Topic</strong><span>Maecenas venenatis faucibus lectus, quis iaculis orci tincidunt auctor.</span></div>
  <div class="a agenda-item" style="left:130px;top:86px"><div class="agenda-no bg-dred">05</div><small>Subtitle of agenda</small><strong>Presentation Topic</strong><span>Maecenas venenatis faucibus lectus, quis iaculis orci tincidunt auctor.</span></div>
  <div class="a agenda-item" style="left:130px;top:123px"><div class="agenda-no bg-black">06</div><small>Subtitle of agenda</small><strong>Presentation Topic</strong><span>Maecenas venenatis faucibus lectus, quis iaculis orci tincidunt auctor.</span></div>
  <div class="a agenda-item" style="left:236px;top:48px"><div class="agenda-no bg-dred">07</div><small>Subtitle of agenda</small><strong>Presentation Topic</strong><span>Maecenas venenatis faucibus lectus, quis iaculis orci tincidunt auctor.</span></div>
  <div class="a agenda-item" style="left:236px;top:86px"><div class="agenda-no bg-black">08</div><small>Subtitle of agenda</small><strong>Presentation Topic</strong><span>Maecenas venenatis faucibus lectus, quis iaculis orci tincidunt auctor.</span></div>
  <div class="a agenda-item" style="left:236px;top:123px"><div class="agenda-no bg-red">09</div><small>Subtitle of agenda</small><strong>Presentation Topic</strong><span>Maecenas venenatis faucibus lectus, quis iaculis orci tincidunt auctor.</span></div>
</section>

<!-- 3 Board -->
<section class="slide">
  <div class="a title">Board Introduction</div><div class="a num">3</div>
  <div class="a photo" role="img" aria-label="Portrait photo of the chief executive" style="left:26px;top:47px;width:48px;height:63px"></div>
  <div class="a bar-red" style="left:26px;top:102px;width:48px;height:8px;font-size:2.8px;font-weight:700;display:flex;align-items:center;justify-content:center">DANIEL R. HOLLOWAY</div>
  <div class="a" style="left:129px;top:46px;width:170px;font-size:9px;font-weight:700;color:var(--black);border-bottom:.8px solid #444;padding-bottom:3px">Welcome from Daniel</div>
  <div class="a b" style="left:129px;top:66px;font-size:4px;color:var(--black)">President and Chief Executive Officer</div>
  <p class="a p" style="left:129px;top:84px;width:172px">Vivamus sollicitudin ac nisi non molestie. Aenean cursus, nisi volutpat vulputate commodo, ex lacus maximus dolor, et hendrerit odio velit eget augue. Integer vel lacinia lacus, ut auctor ante. Vivamus sollicitudin ac nisi non molestie. Aenean cursus, nisi volutpat vulputate commodo, ex lacus maximus dolor, et hendrerit odio velit eget augue. Integer vel lacinia lacus, ut auctor ante.</p>
  <p class="a p" style="left:129px;top:120px;width:172px">Lorem ipsum dolor sit amet, consectetur adipiscing elit. Aenean id lectus vel erat luctus viverra sit amet in diam. Phasellus ut augue vitae orci lobortis fringilla. Integer quis nisl nisi. Vivamus sollicitudin ac nisi non molestie. Aenean cursus, nisi volutpat vulputate commodo, ex lacus maximus dolor, et hendrerit odio velit eget augue. Integer vel lacinia lacus, ut auctor ante.</p>
</section>

<!-- 4 About -->
<section class="slide">
  <div class="a title">About Us</div><div class="a num">4</div>
  <p class="a p" style="left:72px;top:43px;width:208px">Tarnel Holdings, Inc. operates and sells its products and services in the United States. We take pride in seeking harmony with the environment while contributing to the building of contemporary societies, infrastructures, and high-profile projects that improve people's lives and connect them together.</p>
  <p class="a p" style="left:72px;top:66px;width:208px">Through our <span class="red">operating companies</span>, Tarnel Holdings serves major construction markets in the United States in two business segments: ready-mixed concrete and aggregate products. The Company provides its products and services from its operating companies in North and West Texas, Northern California, New Jersey, New York, Washington D.C. and Oklahoma.</p>
  <div class="a bar-red" style="left:72px;top:100px;width:210px;height:11px;font-size:5.6px;font-weight:500;padding-left:6px;display:flex;align-items:center">Value Proposition</div>
  <svg class="a" style="left:80px;top:118px" width="190" height="40" viewBox="0 0 190 40">
    <g fill="#9c9c9c"><circle cx="14" cy="14" r="10"/><circle cx="66" cy="14" r="10"/><circle cx="118" cy="14" r="10"/><circle cx="170" cy="14" r="10"/></g>
    <g fill="none" stroke="#fff" stroke-width="1.2"><circle cx="14" cy="12" r="3.5"/><path d="M12.5 16h3M12.8 18h2.4"/><path d="M62 10v8M66 10v8M70 10v8"/><path d="M62 19l8-8"/><path d="M115 17l6-6M118 11l3 3"/><path d="M166 18l9-9-4 10-1-4z"/></g>
    <g font-size="5" fill="#888" font-family="Roboto,Arial,sans-serif" text-anchor="middle"><text x="14" y="36">The Subtitle</text><text x="66" y="36">The Subtitle</text><text x="118" y="36">The Subtitle</text><text x="170" y="36">The Subtitle</text></g>
  </svg>
</section>

<!-- 5 Quote -->
<section class="slide">
  <div class="a num">5</div>
  <svg class="a" style="left:162px;top:57px" width="26" height="26" viewBox="0 0 26 26"><circle cx="13" cy="13" r="13" fill="var(--red)"/><path d="M8 10h4v4l-2 4H8l2-4H8zM14 10h4v4l-2 4h-2l2-4h-2z" fill="#fff"/></svg>
  <div class="a center" style="left:8px;right:0;top:88px;font-size:9.5px;font-style:italic;font-weight:300;color:#666">Concrete that Advances</div>
  <div class="a center" style="left:72px;width:214px;top:104px;font-size:7px;font-style:italic;font-weight:300;color:#8a8a8a;line-height:1.3">Sustainable and innovative solutions that help achieve environmental, design, and engineering goals</div>
  <div class="a" style="left:62px;width:226px;top:138px;border-top:.6px solid #888"></div>
</section>

<!-- 6 Principles -->
<section class="slide">
  <div class="a title">Operation Principles</div><div class="a num">6</div>
  <svg class="a" style="left:60px;top:50px" width="250" height="60" viewBox="0 0 250 60">
    <circle cx="28" cy="28" r="21" fill="var(--black)"/>
    <circle cx="125" cy="28" r="28" fill="none" stroke="var(--red)" stroke-width="1.5"/><circle cx="125" cy="28" r="24" fill="var(--red)"/>
    <circle cx="222" cy="28" r="21" fill="var(--black)"/>
    <g fill="#fff"><rect x="21" y="24" width="14" height="10" rx="1"/><rect x="25" y="21" width="6" height="3" fill="none" stroke="#fff"/></g>
    <g fill="#fff"><path d="M113 20l12-6 12 6z"/><rect x="115" y="22" width="2.5" height="11"/><rect x="120" y="22" width="2.5" height="11"/><rect x="127" y="22" width="2.5" height="11"/><rect x="132" y="22" width="2.5" height="11"/><rect x="112" y="34" width="26" height="3"/></g>
    <g fill="#fff"><path d="M211 26l11-5 11 5-11 5z"/><path d="M215 28v5c4 3 10 3 14 0v-5l-7 3z"/></g>
  </svg>
  <div class="a center" style="left:60px;width:56px;top:116px;font-size:6px;font-weight:700;color:var(--black)">Vision</div>
  <div class="a center" style="left:157px;width:56px;top:116px;font-size:6px;font-weight:700;color:var(--black)">Core Values</div>
  <div class="a center" style="left:254px;width:56px;top:116px;font-size:6px;font-weight:700;color:var(--black)">Mission</div>
  <p class="a p center" style="left:58px;width:60px;top:126px;color:#666">But what plays the mischief with this masterly code is the admirable brevity.</p>
  <p class="a p center" style="left:155px;width:60px;top:126px;color:#666">But what plays the mischief with this masterly code is the admirable brevity.</p>
  <p class="a p center" style="left:252px;width:60px;top:126px;color:#666">But what plays the mischief with this masterly code is the admirable brevity.</p>
</section>

<!-- 7 Sustainability -->
<section class="slide">
  <div class="a title">Sustainability Strategy</div><div class="a num">7</div>
  <p class="a p dk" style="left:32px;top:36px;width:298px;font-size:4.3px">Tarnel Holdings recognizes the inherent value in aggressively supporting sustainable construction and green building initiatives. Through our high performance, low CO₂ concrete mixes (<b class="red">RX Technology®</b>) and Certified Concrete Sustainability Specialists (CCSS), we continue to contribute to the building of projects that are environmentally responsible, cost-effective and healthy places to live and work.</p>
  <svg class="a" style="left:32px;top:68px" width="300" height="58" viewBox="0 0 300 58">
    <g fill="none" stroke="#888" stroke-width=".7"><circle cx="22" cy="12" r="10"/><circle cx="74" cy="12" r="10"/><circle cx="126" cy="12" r="10"/><circle cx="178" cy="12" r="10"/><circle cx="230" cy="12" r="10"/><circle cx="282" cy="12" r="10"/>
    <path d="M17 15a4 4 0 0 1 2-7 5 5 0 0 1 8 3h-10M70 10a4 4 0 0 1 8 0l1-2M78 14a4 4 0 0 1-8 0l-1 2M122 8h8v8h-8zM173 14l6-5 3 3M223 12h14M230 5v14M278 9l8 6M278 15l8-6"/></g>
    <g font-family="Roboto,Arial,sans-serif" text-anchor="middle"><g fill="var(--red)" font-size="4.6" font-weight="700"><text x="22" y="31">CO₂ emission</text><text x="74" y="31">Recyclable</text><text x="126" y="31">Cost benefits</text><text x="178" y="31">Reduces storm</text><text x="230" y="31">Energy efficient</text><text x="282" y="31">Durability</text></g>
    <g fill="#777" font-size="3.2"><text x="22" y="37">Lorem ipsum dolor sit</text><text x="22" y="41">amet, consectetr adis</text><text x="22" y="45">piscing ult adis pis</text><text x="74" y="37">Lorem ipsum dolor sit</text><text x="74" y="41">amet, consectetr adis</text><text x="74" y="45">piscing ult adis pis</text><text x="126" y="37">Lorem ipsum dolor sit</text><text x="126" y="41">amet, consectetr adis</text><text x="126" y="45">piscing ult adis pis</text><text x="178" y="37">Lorem ipsum dolor sit</text><text x="178" y="41">amet, consectetr adis</text><text x="178" y="45">piscing ult adis pis</text><text x="230" y="37">Lorem ipsum dolor sit</text><text x="230" y="41">amet, consectetr adis</text><text x="230" y="45">piscing ult adis pis</text><text x="282" y="37">Lorem ipsum dolor sit</text><text x="282" y="41">amet, consectetr adis</text><text x="282" y="45">piscing ult adis pis</text></g></g>
  </svg>
  <div class="a bar-red" style="left:30px;top:148px;width:307px;height:9px;font-size:5px;font-weight:700;padding-left:3px;display:flex;align-items:center">CONCRETE IS THE FUTURE OF SUSTAINABLE CONSTRUCTION</div>
  <p class="a p dk" style="left:32px;top:161px;width:300px;font-size:4.2px">Increasingly, concrete is being recognized for its life cycle environmental and economical benefits, from extraction and production, to construction, maintenance and disposal. There are solid facts that make concrete the right choice for effective sustainable development.</p>
</section>

<!-- 8 Process -->
<section class="slide">
  <div class="a title">The Process</div><div class="a num">8</div>
  <div class="a" style="left:305px;top:3px;width:28px;height:16px;border-radius:3px;background:#1f4f9c"></div>
  <div class="a" style="left:8px;right:0;top:35px;height:60px;background:var(--pale)"></div>
  <svg class="a" style="left:14px;top:40px" width="330" height="50" viewBox="0 0 330 50">
    <g fill="none" stroke="#666" stroke-width="1"><path d="M42 15a8 8 0 0 1 16 0M50 15l3-5"/><path d="M126 8l10 12M136 8l-10 12"/><circle cx="212" cy="12" r="4"/><circle cx="219" cy="17" r="3"/><path d="M294 17h12l2-5M296 17v-5h6"/></g>
    <g fill="var(--red)"><path d="M75 10h18v-4l8 7-8 7v-4H75z"/><path d="M158 10h18v-4l8 7-8 7v-4h-18z"/><path d="M240 10h18v-4l8 7-8 7v-4h-18z"/></g>
    <g font-family="Roboto,Arial,sans-serif" font-size="3.6" fill="#555" text-anchor="middle"><text x="50" y="32">At vero eos et accusamus</text><text x="50" y="37">et iusto odio <tspan font-weight="700">dignissimos</tspan></text><text x="131" y="32">At vero eos et accusamus</text><text x="131" y="37">et iusto odio <tspan font-weight="700">dignissimos</tspan></text><text x="215" y="32">At vero eos et accusamus</text><text x="215" y="37">et iusto odio <tspan font-weight="700">dignissimos</tspan></text><text x="299" y="32">At vero eos et accusamus</text><text x="299" y="37">et iusto odio <tspan font-weight="700">dignissimos</tspan></text></g>
  </svg>
  <div class="a" style="left:14px;top:107px;width:126px;font-size:7.5px;font-weight:700;color:var(--black);border-bottom:.6px solid #444;padding-bottom:3px">Subheading Description</div>
  <svg class="a" style="left:14px;top:126px" width="130" height="40" viewBox="0 0 130 40"><g stroke="var(--red)" stroke-width=".8" fill="none"><path d="M2 3l1.5 1.5L6 1M2 11l1.5 1.5L6 9M2 19l1.5 1.5L6 17M2 27l1.5 1.5L6 25"/></g><g font-family="Roboto,Arial,sans-serif" font-size="3.8" fill="#555"><text x="10" y="4.5">Lorem ipsum dolor sit. Amet, ligula suspendisse.</text><text x="10" y="12.5">Nulla pretium, rhoncus. Tempor fermentum.</text><text x="10" y="20.5">Lorem ipsum dolor sit. Amet, ligula suspendisse.</text><text x="10" y="28.5">Nulla pretium, rhoncus. Tempor fermentum.</text></g></svg>
  <p class="a p dk" style="left:14px;top:166px;width:130px">Lorem ipsum dolor sit amet, consectetur adipiscing elit. Etiam et libero quis risus finibus sollicitudin nec vel nisl. Praesent condimentum arcu sed congue bibendum.</p>
  <svg class="a" style="left:155px;top:105px" width="190" height="88" viewBox="0 0 190 88">
    <g font-family="Roboto,Arial,sans-serif" font-size="4" fill="#555"><text x="0" y="5">6</text><text x="0" y="17">5</text><text x="0" y="29">4</text><text x="0" y="41">3</text><text x="0" y="53">2</text><text x="0" y="65">1</text><text x="0" y="77">0</text><text x="27" y="83">2013</text><text x="72" y="83">2014</text><text x="117" y="83">2015</text><text x="162" y="83">2016</text></g>
    <path d="M8 75h180" stroke="#888" stroke-width=".5"/>
    <g fill="var(--red)"><rect x="20" y="28" width="8" height="47"/><rect x="65" y="42" width="8" height="33"/><rect x="110" y="39" width="8" height="36"/><rect x="155" y="26" width="8" height="49"/></g>
    <g fill="#bdbdbd"><rect x="29" y="50" width="8" height="25"/><rect x="74" y="25" width="8" height="50"/><rect x="119" y="61" width="8" height="14"/><rect x="164" y="45" width="8" height="30"/></g>
    <g fill="var(--black)"><rect x="38" y="56" width="8" height="19"/><rect x="83" y="53" width="8" height="22"/><rect x="128" y="45" width="8" height="30"/><rect x="173" y="18" width="8" height="57"/></g>
  </svg>
</section>

<!-- 9 Curve -->
<section class="slide">
  <div class="a title">Upward Sloping Curve</div><div class="a num">9</div>
  <svg class="a" style="left:40px;top:40px" width="200" height="145" viewBox="0 0 200 145">
    <path d="M14 2v131h184" fill="none" stroke="#a0b4d0" stroke-width=".6"/>
    <text x="8" y="85" transform="rotate(-90 8 85)" font-family="Roboto,Arial,sans-serif" font-size="3.6" fill="#666">You can edit this text</text>
    <rect x="66" y="8" width="68" height="125" fill="#d0d0d0"/>
    <text x="70" y="17" font-family="Roboto,Arial,sans-serif" font-size="6" fill="#333">Description</text>
    <text x="70" y="24" font-family="Roboto,Arial,sans-serif" font-size="3.2" fill="#555">Contrary to popular belief, Lorem</text>
    <text x="70" y="28" font-family="Roboto,Arial,sans-serif" font-size="3.2" fill="#555">Ipsum is not simply random text.</text>
    <rect x="17" y="100" width="34" height="31" fill="#ef6b73"/><rect x="53" y="92" width="34" height="39" fill="#d61f2c"/><rect x="89" y="80" width="34" height="51" fill="#b3121c"/><rect x="125" y="64" width="34" height="67" fill="#8f8f8f"/><rect x="161" y="44" width="34" height="87" fill="var(--black)"/>
    <path d="M20 88C80 85 130 70 184 30" fill="none" stroke="#888" stroke-width="4"/><path d="M178 24l12-2-5 11z" fill="#888"/>
    <text x="90" y="142" font-family="Roboto,Arial,sans-serif" font-size="3.6" fill="#666">You can edit this text</text>
  </svg>
  <div class="a" style="left:245px;top:92px;width:90px;font-size:3.8px;line-height:1.5;color:#444">• This is a sample text here.<br>• Insert your desired text here.<br>• This is a sample text here.<br>• Insert your desired text here. This is a<br>&nbsp;&nbsp;sample text here.</div>
</section>

<!-- 10 Solutions -->
<section class="slide">
  <div class="a title">Our Solutions</div><div class="a num">10</div>
  <div class="a" style="left:26px;top:37px;width:154px;height:133px;border:.8px solid #bbb;display:grid;grid-template-columns:1fr 1fr;grid-template-rows:1fr 1fr">
    <div style="border-right:.8px solid #bbb;border-bottom:.8px solid #bbb;text-align:center;padding-top:16px;font-size:5.4px;color:#555"><svg width="18" height="14" viewBox="0 0 18 14"><path d="M2 3h4l6 8h4M2 11h4l6-8h4M14 1l2 2-2 2M14 9l2 2-2 2" fill="none" stroke="#999"/></svg><br>Ready-Mixed<br>Concrete</div>
    <div style="border-bottom:.8px solid #bbb;text-align:center;padding-top:16px;font-size:5.4px;color:#555"><svg width="18" height="14" viewBox="0 0 18 14"><rect x="5" y="1" width="9" height="12" fill="none" stroke="#999"/><path d="M7 4h5M7 7h5M7 10h5" stroke="#999"/></svg><br>Aggregates</div>
    <div style="border-right:.8px solid #bbb;text-align:center;padding-top:16px;font-size:5.4px;color:#555"><svg width="18" height="14" viewBox="0 0 18 14"><circle cx="8" cy="6" r="5" fill="none" stroke="#999"/><path d="M12 10l4 4M8 3v6M5 6h6" stroke="#999"/></svg><br>Value-Added<br>Services</div>
    <div style="text-align:center;padding-top:16px;font-size:5.4px;color:#555"><svg width="18" height="14" viewBox="0 0 18 14"><path d="M9 1l2.2 4.4 4.8.6-3.5 3.3.9 4.7L9 11.8 4.6 14l.9-4.7L2 6l4.8-.6z" fill="none" stroke="#999"/></svg><br>Specialty<br>Products/Solutions</div>
  </div>
  <div class="a" style="left:202px;top:38px;width:126px">
    <div class="b" style="font-size:5.6px;color:var(--black)">Ready-Mixed Concrete</div>
    <p class="p" style="margin:3px 0 6px">Custom mix designs tailored to a particular application. In addition, through our RX Technology®, we supply alternative materials and mix designs that result in lower CO₂ emissions.</p>
    <div class="b" style="font-size:5.6px;color:var(--black)">Aggregates</div>
    <p class="p" style="margin:3px 0 6px">We produce crushed stone aggregates, sand and gravel from nine aggregates facilities located in New Jersey, Oklahoma, and Texas.</p>
    <div class="b" style="font-size:5.6px;color:var(--black)">Value-Added Services</div>
    <p class="p" style="margin:3px 0 6px">We provide a variety of services in connection with our sale of ready-mixed concrete that can help reduce our customers' in-place cost of concrete.</p>
    <div class="b" style="font-size:5.6px;color:var(--black)">Specialty Products/Solutions</div>
    <p class="p" style="margin-top:3px">Through strategic partnerships, Tarnel Holdings supplies custom mixes, specialty products and solutions that can help developers and architects meet their project challenges.</p>
  </div>
</section>

<!-- 11 List point services -->
<section class="slide">
  <div class="a title">List Point Services</div><div class="a num">11</div>
  <svg class="a" style="left:20px;top:46px" width="320" height="140" viewBox="0 0 320 140">
    <g><circle cx="30" cy="20" r="12" fill="var(--black)"/><circle cx="102" cy="20" r="12" fill="#8f8f8f"/><circle cx="174" cy="20" r="12" fill="#bdbdbd"/><circle cx="246" cy="20" r="12" fill="var(--red)"/>
    <circle cx="30" cy="84" r="12" fill="var(--dark-red)"/><circle cx="102" cy="84" r="12" fill="var(--black)"/><circle cx="174" cy="84" r="12" fill="#8f8f8f"/><circle cx="246" cy="84" r="12" fill="#cfcfcf"/></g>
    <g fill="none" stroke="#fff" stroke-width="1.2"><path d="M25 24l8-8M27 16h6v6"/><path d="M98 15h8v5a4 4 0 0 1-8 0z"/><circle cx="174" cy="18" r="4"/><path d="M174 22v5"/><circle cx="246" cy="20" r="5"/><circle cx="246" cy="20" r="1.5"/><path d="M26 86h8M30 78v6M27 80l6 0"/><path d="M98 88v-6M102 88v-9M106 88v-4"/><rect x="169" y="80" width="10" height="7"/><path d="M241 88l4-4 3 2 4-5"/></g>
    <g font-family="Roboto,Arial,sans-serif" text-anchor="middle"><g font-size="3.4" font-weight="700" fill="#333"><text x="30" y="41">Item | Subtitle Here</text><text x="102" y="41">Item | Subtitle Here</text><text x="174" y="41">Item | Subtitle Here</text><text x="246" y="41">Item | Subtitle Here</text><text x="30" y="105">Item | Subtitle Here</text><text x="102" y="105">Item | Subtitle Here</text><text x="174" y="105">Item | Subtitle Here</text><text x="246" y="105">Item | Subtitle Here</text></g>
    <g font-size="2.8" fill="#999"><text x="30" y="48">Gepla ibpsum vubdis vendiae</text><text x="30" y="52">quantum temaii son exper</text><text x="102" y="48">Gepla ibpsum vubdis vendiae</text><text x="102" y="52">quantum temaii son exper</text><text x="174" y="48">Gepla ibpsum vubdis vendiae</text><text x="174" y="52">quantum temaii son exper</text><text x="246" y="48">Gepla ibpsum vubdis vendiae</text><text x="246" y="52">quantum temaii son exper</text><text x="30" y="112">Gepla ibpsum vubdis vendiae</text><text x="30" y="116">quantum temaii son exper</text><text x="102" y="112">Gepla ibpsum vubdis vendiae</text><text x="102" y="116">quantum temaii son exper</text><text x="174" y="112">Gepla ibpsum vubdis vendiae</text><text x="174" y="116">quantum temaii son exper</text><text x="246" y="112">Gepla ibpsum vubdis vendiae</text><text x="246" y="116">quantum temaii son exper</text></g></g>
  </svg>
</section>

<!-- 12 US Maps -->
<section class="slide">
  <div class="a title">US Maps</div><div class="a num">12</div>
  <div class="a" style="left:24px;top:52px;width:0;height:0;border-left:4px solid var(--red);border-bottom:4px solid transparent"></div>
  <div class="a b" style="left:24px;top:60px;width:100px;font-size:5.8px;color:var(--black);line-height:1.2">Ut wisi enim ad minim veniam, quis nostrud exerci</div>
  <p class="a p" style="left:24px;top:76px;width:96px"><b class="dk">Ut wisi enim</b> ad minim veniam, quis nostrud exerci tation ullamcorper nisl exerci tincidunt ut laoreet dolore magna aliquam erat volutpat. Ut wisi enim ad minim veniam, quis nostrud exerci. exerci tation ullamcorper nibh euismod tincidunt ut laoreet.</p>
  <div class="a bar-red" style="left:24px;top:124px;width:20px;height:5px;border-radius:3px;font-size:2.4px;display:flex;align-items:center;justify-content:center">ReadMore</div>
  <div class="a" role="img" aria-label="Map of the United States with highlighted operating states" style="left:150px;top:50px;width:170px;height:108px;border-radius:22px 30px 26px 40px;background:linear-gradient(160deg,#e4e4e4,#c9c9c9)"></div>
  <div class="a" style="left:220px;top:68px;width:20px;height:14px;background:#555"></div>
  <div class="a bar-red" style="left:218px;top:53px;width:62px;height:11px;font-size:2.8px;padding:2px 3px;line-height:1.3">Ut wisi enim ad minim veniam, quis nostrud exerci tation</div>
  <svg class="a" style="left:168px;top:72px" width="110" height="50" viewBox="0 0 110 50"><g fill="#fff" stroke="#555" stroke-width=".8"><circle cx="6" cy="6" r="2"/><circle cx="24" cy="22" r="2"/><circle cx="62" cy="6" r="2" stroke="var(--red)"/><circle cx="78" cy="26" r="2"/></g></svg>
</section>

<!-- 13 World Maps -->
<section class="slide">
  <div class="a title">World Maps</div><div class="a num">13</div>
  <div class="a" role="img" aria-label="World map highlighting Europe, US, Africa and Asia" style="left:26px;top:70px;width:176px;height:90px;border-radius:30px 40px 24px 36px;background:linear-gradient(100deg,#1a1a1a 0 28%,#a8a8a8 28% 38%,#c8102e 38% 46%,#b0b0b0 46%)"></div>
  <svg class="a" style="left:204px;top:76px" width="6" height="88" viewBox="0 0 6 88"><path d="M3 3v82" stroke="var(--red)" stroke-width=".6" stroke-dasharray="1.5 1"/><path d="M0 4l3-4 3 4zM0 84l3 4 3-4z" fill="var(--red)"/></svg>
  <div class="a" style="left:222px;top:80px;width:48px"><div style="font-size:12px;color:#bbb;font-weight:300">15%</div><div class="b" style="font-size:5.4px;color:var(--black)">Europe</div><p class="p" style="font-size:2.8px;margin-top:2px">The quick brown fox jumps over a lazy dog. Cox flow by vexed MTV ex. ad quiz pang. Junk MTV quiz graced by fox whelps.</p></div>
  <div class="a" style="left:280px;top:80px;width:48px"><div style="font-size:12px;color:#bbb;font-weight:300">30%</div><div class="b" style="font-size:5.4px;color:var(--black)">US</div><p class="p" style="font-size:2.8px;margin-top:2px">The quick brown fox jumps over a lazy dog. Cox flow by vexed MTV ex. ad quiz pang. Junk MTV quiz graced by fox whelps.</p></div>
  <div class="a" style="left:222px;top:128px;width:48px"><div style="font-size:12px;color:#bbb;font-weight:300">20%</div><div class="b" style="font-size:5.4px;color:var(--black)">Africa</div><p class="p" style="font-size:2.8px;margin-top:2px">The quick brown fox jumps over a lazy dog. Cox flow by vexed MTV ex. ad quiz pang. Junk MTV quiz graced by fox whelps.</p></div>
  <div class="a" style="left:280px;top:128px;width:48px"><div style="font-size:12px;color:#bbb;font-weight:300">35%</div><div class="b" style="font-size:5.4px;color:var(--black)">Asia</div><p class="p" style="font-size:2.8px;margin-top:2px">The quick brown fox jumps over a lazy dog. Cox flow by vexed MTV ex. ad quiz pang. Junk MTV quiz graced by fox whelps.</p></div>
</section>

<!-- 14 Single list -->
<section class="slide">
  <div class="a title">Traditional Single List</div><div class="a num">14</div>
  <p class="a" style="left:24px;top:34px;width:260px;font-size:5px;line-height:1.4;color:#bbb"><b style="color:var(--black)">Contrary to popular belief,</b> Lorem Ipsum is not simply random text. It has roots in a piece of classical Latin literature from 45 BC</p>
  <div class="a" style="left:24px;width:272px;top:58px;border-top:.7px solid var(--red)"></div>
  <svg class="a" style="left:40px;top:76px" width="10" height="60" viewBox="0 0 10 60"><g fill="none" stroke="var(--red)" stroke-width="1"><path d="M1 4l3 3 6-6M1 26l3 3 6-6M1 48l3 3 6-6"/></g></svg>
  <p class="a p" style="left:56px;top:76px;width:250px;font-size:4.6px;color:#777">Quisque libero purus, bibendum nec quam sit amet, porta interdum ex. Aliquam erat volutpat. Quisque commodo lacus sed lectus condimentum cursus.</p>
  <p class="a p" style="left:56px;top:98px;width:250px;font-size:4.6px;color:#777">Praesent a diam neque. Aenean ultricies eu orci id euismod. Integer eleifend, lacus quis tincidunt posuere, nisl neque sodales justo, quis suscipit libero odio ut quam.</p>
  <p class="a p" style="left:56px;top:120px;width:250px;font-size:4.6px;color:#777">Nam auctor, leo a volutpat rhoncus, erat arcu dignissim velit, in aliquet erat metus quis tellus. Vestibulum nec lobortis augue, at interdum nisl.</p>
  <p class="a p" style="left:34px;top:150px;width:270px;font-size:5px;color:#999">Cras laoreet mauris eget pharetra auctor. Donec lacinia est id euismod eleifend. Quisque condimentum varius ullamcorper. Nunc quam libero, feugiat ut ante eu, ultrices efficitur erat.</p>
</section>

<!-- 15 Two column -->
<section class="slide">
  <div class="a title">Two Column Text</div><div class="a num">15</div>
  <p class="a p dk" style="left:24px;top:34px;width:312px;font-size:4.8px;color:#555"><b style="color:var(--black)">Contrary to popular belief,</b> Lorem Ipsum is not simply random text. It has roots in a piece of classical Latin literature from 45 BC. Cras laoreet mauris eget pharetra auctor. Donec lacinia est id euismod eleifend. Quisque condimentum varius ullamcorper.</p>
  <p class="a p" style="left:24px;top:62px;width:148px">Lorem ipsum dolor sit amet, consectetur adipiscing elit. Etiam et libero quis risus finibus sollicitudin nec vel nisl. Praesent condimentum arcu sed congue bibendum. Nulla facilisi. Curabitur pretium ante tincidunt, rhoncus ante sed, vulputate tortor. Sed molestie sodales purus, et aliquam velit porttitor sed. Quisque vulputate elit nec semper pharetra. Suspendisse finibus sed ante vitae eleifend. Donec eleifend egestas commodo. Nam lorem dui, vehicula in tempus tincidunt, consequat at ante. Morbi feugiat nisi sem, a imperdiet velit aliquet vel.<br><br>Mauris dapibus urna ut ex commodo, non elementum libero feugiat. Quisque libero purus, bibendum nec quam sit amet, porta interdum ex. Aliquam erat volutpat. Quisque commodo lacus sed lectus condimentum cursus. Praesent a diam neque. Aenean ultricies eu orci id euismod. Integer eleifend, lacus quis tincidunt posuere, nisl neque sodales justo, quis suscipit libero odio ut quam. Nam auctor, leo a volutpat rhoncus, erat arcu dignissim velit, in aliquet erat metus quis tellus.</p>
  <p class="a p" style="left:188px;top:62px;width:148px">Iaculis orci tincidunt auctor. Quisque mollis orci nec orci placerat, sit amet semper diam lacinia. Vivamus vel massa lectus. Cras laoreet mauris eget pharetra auctor. Donec lacinia est id euismod eleifend. Quisque condimentum varius ullamcorper.<br><br>Nunc quam libero, feugiat ut ante eu, ultrices efficitur erat. Duis sit amet est convallis, pretium libero eu, mollis tortor. Morbi rutrum, diam vel neque suscipit, lectus velit congue magna, quis fermentum justo arcu non purus. Lorem ipsum dolor sit amet, consectetur adipiscing elit. Aenean id lectus vel erat luctus viverra sit amet in diam. Phasellus ut augue vitae orci lobortis fringilla. Integer quis nisl nisi.</p>
</section>

<!-- 16 Three column -->
<section class="slide">
  <div class="a title">Three Column Text</div><div class="a num">16</div>
  <p class="a p dk" style="left:24px;top:34px;width:312px;font-size:4.8px;color:#555"><b style="color:var(--black)">Contrary to popular belief,</b> Lorem Ipsum is not simply random text. It has roots in a piece of classical Latin literature from 45 BC. Cras laoreet mauris eget pharetra auctor. Donec lacinia est id euismod eleifend. Quisque condimentum varius ullamcorper.</p>
  <p class="a p" style="left:24px;top:68px;width:94px">Lorem ipsum dolor sit amet, consectetur adipiscing elit. Etiam et libero quis risus finibus sollicitudin nec vel nisl. Praesent condimentum arcu sed congue bibendum. Nulla facilisi. Curabitur pretium ante tincidunt, rhoncus ante sed, vulputate tortor.<br><br>Sed molestie sodales purus, et aliquam velit porttitor sed. Quisque vulputate elit nec semper pharetra. Suspendisse finibus sed ante vitae eleifend. Donec eleifend egestas commodo. Nam lorem dui, vehicula in tempus tincidunt, consequat at ante.</p>
  <p class="a p" style="left:125px;top:68px;width:94px">Quisque commodo lacus sed lectus condimentum cursus. Praesent a diam neque. Aenean ultricies eu orci id euismod. Integer eleifend, lacus quis tincidunt posuere, nisl neque sodales justo, quis suscipit libero odio ut quam. Nam auctor, leo a volutpat rhoncus, erat arcu dignissim velit.<br><br>Maecenas venenatis faucibus lectus, quis iaculis orci tincidunt auctor. Quisque mollis orci nec orci placerat, sit amet semper diam lacinia.</p>
  <p class="a p" style="left:226px;top:68px;width:94px">Nam auctor, leo a volutpat rhoncus, erat arcu dignissim velit, in aliquet erat metus quis tellus. Vestibulum nec lobortis augue, at interdum nisl. Vivamus vel massa lectus. Cras laoreet mauris eget pharetra auctor. Donec lacinia est id euismod.<br><br>Maecenas venenatis faucibus lectus, quis iaculis orci tincidunt auctor. Quisque mollis orci nec orci placerat, sit amet semper diam lacinia.</p>
</section>

<!-- 17 Team -->
<section class="slide">
  <div class="a title">The Management Team</div><div class="a num">17</div>
  <ol class="a" style="left:24px;top:40px;width:145px;font-size:3.2px;color:#555;line-height:1.55;padding-left:6px">
    <li>Daniel R. Holloway – President and Chief Executive Officer</li>
    <li>Marcus T. Ellery – Senior Vice President and Chief Financial Officer</li>
    <li>Glen Harwick – Senior Vice President and Chief Operating Officer</li>
    <li>Simon P. Kearn – Senior Vice President, General Counsel and Corporate Secretary</li>
    <li>Trevor Ashdale – Vice President and Chief Accounting Officer</li>
    <li>Owen L. Pratt – Vice President</li>
  </ol>
  <ol class="a" start="7" style="left:180px;top:40px;width:155px;font-size:3.2px;color:#555;line-height:1.55;padding-left:8px">
    <li>Victor H. Lindell – Vice President, Marketing and Sales</li>
    <li>Curtis B. Fenwick – Vice President, Human Resources</li>
    <li>Arne L. Westby – Executive Vice President, South-East Division</li>
    <li>Neil Garland – Vice President and General Manager, West Region</li>
    <li>Colin W. Ramsey – Vice President and General Manager of Halvorsen Ready Mix</li>
  </ol>
  <div class="a team-strip">
    <div class="team-row top">
      <div class="team-photo" role="img" aria-label="Team member portrait 1"><b>01</b></div>
      <div class="team-photo" role="img" aria-label="Team member portrait 2"><b>02</b></div>
      <div class="team-photo" role="img" aria-label="Team member portrait 3"><b>03</b></div>
      <div class="team-photo" role="img" aria-label="Team member portrait 4"><b>04</b></div>
      <div class="team-photo" role="img" aria-label="Team member portrait 5"><b>05</b></div>
      <div class="team-photo" role="img" aria-label="Team member portrait 6"><b>06</b></div>
    </div>
    <div class="team-row">
      <div class="team-photo" role="img" aria-label="Team member portrait 7"><b>07</b></div>
      <div class="team-photo" role="img" aria-label="Team member portrait 8"><b>08</b></div>
      <div class="team-photo" role="img" aria-label="Team member portrait 9"><b>09</b></div>
      <div class="team-photo" role="img" aria-label="Team member portrait 10"><b>10</b></div>
      <div class="team-photo" role="img" aria-label="Team member portrait 11"><b>11</b></div>
    </div>
  </div>
</section>

<!-- 18 Annual report -->
<section class="slide">
  <div class="a title">Annual Report Table</div><div class="a num">18</div>
  <svg class="a" style="left:14px;top:56px" width="70" height="30" viewBox="0 0 70 30"><g fill="none" stroke="var(--black)" stroke-width="1.3"><circle cx="14" cy="14" r="12"/><circle cx="50" cy="14" r="12"/><path d="M9 9l10 10M19 9L9 19M7 8l4 0M50 7v14M47 7a3 3 0 0 0 6 0"/></g></svg>
  <div class="a b red" style="left:88px;top:57px;font-size:6px">Company budget files 2017</div>
  <p class="a p" style="left:88px;top:66px;width:96px;font-size:2.8px">Lorem ipsum dolor sit amet, ligula suspendisse nulla pretium, rhoncus tempor fermentum, enim integer ad vestibulum volutpat. Nisl rhoncus turpis est, vel elit, congue wisi enim nunc ultricies sit, magna tincidunt.</p>
  <table class="a report" style="left:14px;top:88px;width:200px;border-collapse:collapse">
    <tr><th>Nisi rhoncus turpis est</th><th>2014</th><th>2015</th><th>2016</th><th>2017</th></tr>
    <tr><td>Praesent condimentum arcu</td><td>4,456</td><td>4,456</td><td>4,456</td><td>4,456</td></tr>
    <tr><td>Praesent condimentum arcu</td><td>5,345</td><td>5,345</td><td>5,345</td><td>5,345</td></tr>
    <tr><td>Praesent condimentum arcu</td><td>6,567</td><td>6,567</td><td>6,567</td><td>6,567</td></tr>
    <tr><td>Praesent condimentum arcu</td><td>7,678</td><td>7,678</td><td>7,678</td><td>7,678</td></tr>
    <tr><td>Praesent condimentum arcu</td><td>8,789</td><td>8,789</td><td>8,789</td><td>8,789</td></tr>
    <tr><td class="b red" style="font-size:4px">CHANGE 20%</td><td></td><td></td><td></td><td></td></tr>
  </table>
  <div class="a stats">
    <h4>STATS MANAGER</h4>
    <div class="stat">THIS YEAR<b>17,250</b></div>
    <div class="stat">THIS MONTH<b>3,000</b></div>
    <div class="stat">THIS WEEK<b>450</b></div>
    <div class="stat">TODAY<b>225</b></div>
  </div>
</section>

</main>
</body>
</html>
```